New website for a commercial real estate consulting company

What we’re looking for in a new web site:
• Desktop and mobile friendly
• Clear navigation
• Strong graphics
• Professional appearance
• The ability to update it ourselves
• Site is for information purposes only – no transactions required
• Traffic counts – number of visits per page?
• A firm quote on costs to develop and launch
• SSL
Attached is a copy of the revised text we propose to use, including our new logo. (The pagination can be different than as shown.)
Our current website address is www.tamblinvaleadvisory.ca

```html
<!DOCTYPE html>
<html lang="en">
<head>
<meta charset="utf-8">
<title>What We Do – Tamblin Vale Advisory</title>
<link href="https://fonts.googleapis.com/css2?family=Montserrat:wght@400;500&display=swap" rel="stylesheet">
<style>
  :root {
    --brand-blue: #2b3890;
    --nav-grey: #8a8a8a;
    --body-grey: #8f8f8f;
    --menu-bg: #efefef;
    --teal: #12c9c3;
    --white: #ffffff;
  }
  * { margin: 0; padding: 0; box-sizing: border-box; }
  html, body { width: 1200px; height: 1200px; overflow: hidden; background: var(--white); }
  body { font-family: "Montserrat", Arial, sans-serif; position: relative; }

  .site-header { position: absolute; top: 0; left: 0; width: 1200px; height: 114px; background: var(--white); z-index: 2; }
  .brand { position: absolute; left: 86px; top: 38px; display: flex; align-items: center; gap: 8px; }
  .brand-mark { width: 16px; height: 16px; background: var(--brand-blue); }
  .brand-name { font-size: 14px; font-weight: 500; color: var(--brand-blue); letter-spacing: 1.5px; text-transform: uppercase; line-height: 1.25; }

  .main-nav { position: absolute; top: 52px; right: 74px; display: flex; gap: 28px; }
  .main-nav a { font-size: 10.5px; letter-spacing: 1.4px; color: var(--nav-grey); text-decoration: none; text-transform: uppercase; }
  .main-nav a.active { color: var(--brand-blue); }

  .submenu { position: absolute; left: 712px; top: 78px; width: 219px; height: 149px; background: var(--menu-bg); padding-top: 18px; z-index: 3; }
  .submenu::before { content: ""; position: absolute; top: -6px; left: 44px; border: 6px solid transparent; border-top: 0; border-bottom-color: var(--menu-bg); }
  .submenu a { display: block; padding-left: 13px; height: 31px; font-size: 10.5px; letter-spacing: 1.4px; color: var(--nav-grey); text-decoration: none; text-transform: uppercase; }
  .submenu a.active { color: var(--brand-blue); }

  .hero { position: absolute; top: 114px; left: 0; width: 1200px; height: 530px;
    background: radial-gradient(ellipse at 50% 70%, #d9dde0 0%, #a9afb4 35%, #3c4148 70%, #1c1f24 100%); }
  .hero h1 { position: absolute; top: 215px; width: 100%; text-align: center; color: var(--white);
    font-size: 52px; font-weight: 500; text-shadow: 0 2px 6px rgba(0,0,0,.55); }

  .service { position: absolute; top: 644px; left: 0; width: 1200px; height: 495px; }
  .service h2 { position: absolute; top: 40px; width: 100%; text-align: center; font-size: 43px; font-weight: 400; color: var(--brand-blue); }
  .service-text { position: absolute; left: 87px; top: 140px; width: 510px; font-size: 14.2px; line-height: 21px; color: var(--body-grey); }
  .service-text p { margin-bottom: 21px; }
  .service-text ul { list-style: none; }
  .service-text li { position: relative; padding-left: 31px; }
  .service-text li::before { content: "•"; position: absolute; left: 0; font-size: 10px; }
  .service-photo { position: absolute; left: 611px; top: 141px; width: 527px; height: 297px;
    background: linear-gradient(160deg, #b9cbe0 0%, #dfe6ee 45%, #9aa3a8 75%, #6e8a5a 100%); }

  .band-buyers { position: absolute; top: 1139px; left: 0; width: 1200px; height: 61px; background: var(--teal); overflow: hidden; }
  .band-buyers h2 { position: absolute; top: 40px; width: 100%; text-align: center; font-size: 43px; font-weight: 400; color: var(--brand-blue); }
</style>
</head>
<body>
  <header class="site-header">
    <div class="brand">
      <span class="brand-mark"></span>
      <span class="brand-name">Tamblin Vale<br>Advisory</span>
    </div>
    <nav class="main-nav">
      <a href="#">Home</a>
      <a href="#">Who We Are</a>
      <a href="#" class="active">What We Do</a>
      <a href="#">Contact Us</a>
      <a href="#">Industry Events Calendar</a>
    </nav>
  </header>
  <nav class="submenu">
    <a href="#" class="active">For Owners</a>
    <a href="#">For Buyers</a>
    <a href="#">For Lenders</a>
    <a href="#">For Brokers</a>
  </nav>

  <section class="hero" role="img" aria-label="Photo of business people reviewing architectural plans on a table">
    <h1>What We Do</h1>
  </section>

  <section class="service">
    <h2>For Owners</h2>
    <div class="service-text">
      <p>With sixty years of varied and progressive industry experience, we have the expertise to quickly grasp the priorities and challenges of your organization.</p>
      <p>We offer:</p>
      <ul>
        <li>Pre-sale financial due diligence;</li>
        <li>Detailed lease reviews for both pre-sale and lease administration;</li>
        <li>Year-end CAM audits, verification and reconciliation;</li>
        <li>Lease vs buy analysis;</li>
        <li>Asset management;</li>
        <li>Portfolio risk assessments.</li>
      </ul>
    </div>
    <div class="service-photo" role="img" aria-label="Photo of a crawler crane lifting a concrete block on a construction site"></div>
  </section>

  <section class="band-buyers">
    <h2>For Buyers</h2>
  </section>
</body>
</html>
```